Business Card Design

The Amber Hearth is a specialist spit roast catering service, equipped with mobile facilities and professional staff to host your function, inside or out.

We cater for all occasions including weddings, birthdays, corporate functions, sporting events and more.

The Amber Hearth was established in 1983 and is now one of Australia's largest and fastest growing spit roast caterers, with franchises Australia wide, attributing its outstanding success to quality, professionalism and exceptional customer service.

Ridge to Ridge The Amber Hearth is your complete catering solution. We prepare, cook and present the food, allowing you to completely enjoy your function and entertain your guests. We even clean up after ourselves and package any unconsumed foods for your continued enjoyment.

Choose your Amber Hearth menu from premium cuts of pork, lamb, beef, chicken and baked ham, spit roasted to perfection creating mouth watering flavours. All meats are provided by leading local butchers and are cooked on-site to ensure quality and freshness.

Our professionally trained staff also provide complimentary tea and coffee with your function and are pleased to accommodate special dietary requests. The Amber Hearth also provides plates, cups, cutlery and serviettes in the colour of your choice.

Renowned for our generous servings, we never run out of food, for numbers quoted, and what is not consumed, remains with you. We are dedicated to ensuring your function is catered for professionally, with unbeatable value. There is absolutely no compromise on quality, quantity or presentation.

Further options include hot or cold pre-dinner nibbles and Ridge to Ridge The Amber Hearth are equipped to cater for up to 5,000 guests.

Industry/Entity Type

Catering

Contact Information for Business Card

Marek Pellow
PH: 1300 482 917
M: 0412 358 204
Email: northbay@amberhearth.com.au
www.amberhearth.com.au/northbay

Specialist Spit Roast & Event Catering, Australia Wide

```html
<!DOCTYPE html>
<html lang="en">
<head>
<meta charset="utf-8">
<title>The Amber Hearth – Business Cards</title>
<link rel="stylesheet" href="https://fonts.googleapis.com/css2?family=Open+Sans:wght@400;600;800&family=Tinos:ital@1&display=swap">
<style>
  :root {
    --backdrop: #e9e4dd;
    --card: #ffffff;
    --brand-red: #d9614f;
    --tagline-blue: #2f5aa8;
    --ink: #1d1d1d;
    --muted: #555555;
  }
  * { box-sizing: border-box; margin: 0; padding: 0; }
  html, body {
    width: 1200px; height: 913px; overflow: hidden;
    background: var(--backdrop);
    font-family: "Open Sans", Arial, sans-serif;
  }
  .stage {
    width: 1200px; height: 913px;
    display: flex; align-items: center; justify-content: center; gap: 60px;
  }
  .card {
    position: relative;
    width: 525px; height: 300px;
    background: var(--card);
    box-shadow: 0 6px 18px rgba(0,0,0,.18);
  }
  .brand-name {
    font-weight: 800; color: var(--brand-red);
    white-space: nowrap; line-height: 1.1;
  }
  .tagline {
    font-family: "Tinos", "Times New Roman", serif; font-style: italic;
    color: var(--tagline-blue); white-space: nowrap;
  }

  /* Front */
  .card--front .brand-name {
    position: absolute; left: 0; right: 0; top: 100px;
    text-align: center; font-size: 40px;
  }
  .card--front .tagline {
    position: absolute; left: 0; right: 0; top: 170px;
    text-align: center; font-size: 26px;
  }

  /* Back */
  .card--back .brand-name {
    position: absolute; right: 30px; top: 30px; font-size: 24px;
  }
  .card--back .tagline {
    position: absolute; right: 30px; top: 72px; font-size: 14px;
  }
  .card--back .services {
    position: absolute; right: 30px; top: 98px;
    font-family: "Tinos", "Times New Roman", serif; font-style: italic;
    color: var(--brand-red); font-size: 16px; line-height: 1.25; text-align: right;
  }
  .person {
    position: absolute; left: 34px; top: 178px;
  }
  .person-name { font-weight: 800; font-size: 16px; color: var(--ink); }
  .person-role { font-size: 10px; color: var(--muted); }
  .contact {
    position: absolute; left: 34px; top: 222px;
    list-style: none; font-size: 11.5px; line-height: 1.5; color: var(--ink);
  }
  .contact .label { color: var(--brand-red); font-weight: 600; }
  .contact .sep { color: var(--brand-red); margin: 0 6px; }
</style>
</head>
<body>
<main class="stage">
  <section class="card card--front" aria-label="Card front">
    <p class="brand-name">The Amber Hearth</p>
    <p class="tagline">Savour the Occasion...</p>
  </section>

  <section class="card card--back" aria-label="Card back">
    <p class="brand-name">The Amber Hearth</p>
    <p class="tagline">Savour the Occasion...</p>
    <p class="services">Specialist Spit Roast &amp; Event<br>Catering, Australia Wide</p>
    <div class="person">
      <p class="person-name">Marek Pellow</p>
      <p class="person-role">Head Chef / Owner</p>
    </div>
    <ul class="contact">
      <li><span class="label">P:</span> 1300 482 917<span class="sep">•</span><span class="label">M:</span> 0412 358 204</li>
      <li><span class="label">E:</span> northbay@amberhearth.com.au</li>
      <li><span class="label">W:</span> www.amberhearth.com.au/northbay</li>
    </ul>
  </section>
</main>
</body>
</html>
```